11 x 17 Orvanthes Quote

Design the following quote in a poster.

"First say to yourself what you would be; then do what you have to do." - Orvanthes

See here for inspiration - https://prints.mornbrekal.com/

Quote

```html
<!DOCTYPE html>
<html lang="en">
<head>
<meta charset="utf-8">
<title>Orvanthes Quote Poster</title>
<link rel="stylesheet" href="https://fonts.googleapis.com/css2?family=Special+Elite&display=swap">
<style>
  :root {
    --paper: #ffffff;
    --ink: #1c1a1a;
    --accent: #a82a25;
    --accent-text: #ffffff;
  }
  html, body {
    margin: 0;
    padding: 0;
    overflow: hidden;
    background: var(--paper);
  }
  .poster {
    position: relative;
    width: 776px;
    height: 1200px;
    overflow: hidden;
    background: var(--paper);
    font-family: "Special Elite", "Courier New", monospace;
    color: var(--ink);
  }
  .quote-line {
    position: absolute;
    left: 0;
    width: 100%;
    margin: 0;
    text-align: center;
    font-size: 96px;
    line-height: 1;
    white-space: nowrap;
    text-transform: uppercase;
  }
  .quote-line span {
    display: inline-block;
    transform: scaleX(0.74);
  }
  .accent-diamond {
    position: absolute;
    left: 236px;
    top: 480px;
    width: 308px;
    height: 310px;
  }
  .accent-word {
    position: absolute;
    left: 0;
    width: 100%;
    margin: 0;
    text-align: center;
    font-size: 78px;
    line-height: 1;
    color: var(--accent-text);
  }
  .accent-word span {
    display: inline-block;
    transform: scaleX(0.76);
  }
  .attribution {
    position: absolute;
    left: 0;
    top: 1022px;
    width: 100%;
    margin: 0;
    text-align: center;
    font-size: 38px;
    line-height: 1;
    color: var(--accent);
    text-transform: uppercase;
  }
  .attribution span {
    display: inline-block;
    transform: scaleX(0.78);
  }
</style>
</head>
<body>
<main class="poster">
  <blockquote>
    <p class="quote-line" style="top:128px"><span>“First say to</span></p>
    <p class="quote-line" style="top:216px"><span>yourself</span></p>
    <p class="quote-line" style="top:305px"><span>what you</span></p>
    <p class="quote-line" style="top:393px"><span>would be;</span></p>

    <svg class="accent-diamond" viewBox="0 0 308 310" aria-hidden="true">
      <polygon points="154,0 308,152 154,310 0,156" fill="var(--accent)"/>
    </svg>
    <p class="accent-word" style="top:570px"><span>THEN</span></p>
    <p class="accent-word" style="top:636px"><span>DO</span></p>

    <p class="quote-line" style="top:798px"><span>what you</span></p>
    <p class="quote-line" style="top:886px"><span>have to do.”</span></p>
  </blockquote>
  <p class="attribution"><span>Orvanthes</span></p>
</main>
</body>
</html>
```